Business Card Design

We need a business card design for a Executive search firm based in London & the North East called Kelmscott. We specialise in mid - snr level (£50k - £200k) IT placements. Our company colour is navy blue.

Target Market(s)

CEO, HR Director, Sales Director/VP - (35 - 50), well educated, British, European & American

Industry/Entity Type

Business

Contact Information for Business Card

Kelmscott Talent Limited, Simon Trewella
Mobile - 0044 7700 318 642
London Office - Kelmscott House, 17 Birchcombe, Pinner. HA5 3QX
Tel: 00 44 20 718 46203
North East Office – Veltris Centre, Marlowe Lane, Hebburn, NE31 4GT
Tel: 00 44 191 4826053
www.kelmscotttalent-example.com

Also the same details for my Business Partner Ravi Sotkar
with his mobile number as 0044 7700 582731

Requirements
Must have
• must have the same logo

the logo needs to be the same but made sharper

```html
<!DOCTYPE html>
<html lang="en">
<head>
<meta charset="utf-8">
<title>Kelmscott Business Card</title>
<link rel="stylesheet" href="https://fonts.googleapis.com/css2?family=Oswald:wght@500&family=Exo+2:wght@400;500&display=swap">
<style>
  :root {
    --navy: #3e5f86;
    --navy-ink: #3a4f6f;
    --grey: #a8a9ac;
    --grey-dark: #5a5b5e;
    --white: #ffffff;
    --text: #333333;
    --stage: #e4e5e7;
  }
  * { margin: 0; padding: 0; box-sizing: border-box; }
  html, body { width: 1200px; height: 903px; overflow: hidden; }
  body { background: var(--stage); position: relative; }

  .card {
    position: absolute;
    width: 620px;
    height: 354px;
    background: var(--white);
    overflow: hidden;
    box-shadow: 0 6px 18px rgba(0,0,0,0.18);
  }
  .card--front { left: 290px; top: 60px; }
  .card--back  { left: 290px; top: 480px; }

  .band { position: absolute; left: 0; width: 100%; }

  /* Front */
  .front__top    { top: 0; height: 74px; background: var(--navy); }
  .front__rule   { top: 250px; height: 20px; background: var(--grey-dark); }
  .front__bottom { top: 270px; height: 84px; background: var(--navy); }

  .company-name {
    position: absolute;
    font-family: "Exo 2", sans-serif;
    font-weight: 500;
    color: var(--navy-ink);
    letter-spacing: 1px;
    line-height: 1;
    white-space: nowrap;
  }
  .front__name { left: 50%; top: 162px; transform: translate(-50%, -50%); font-size: 42px; }

  /* Back */
  .back__top      { top: 0; height: 22px; background: var(--grey); }
  .back__divider  { top: 112px; height: 24px; background: var(--grey); }
  .back__panel    { position: absolute; left: 400px; top: 136px; width: 220px; height: 184px; background: var(--grey); }

  .offices {
    position: absolute;
    right: 40px;
    top: 46px;
    text-align: right;
    font-family: "Exo 2", sans-serif;
    font-weight: 500;
    font-size: 14px;
    line-height: 1.55;
    color: var(--text);
    letter-spacing: 0.3px;
    white-space: nowrap;
  }

  .back__name { left: 40px; top: 168px; font-size: 34px; }

  .identity {
    position: absolute;
    left: 0;
    top: 232px;
    width: 400px;
    height: 88px;
    background: var(--navy);
    padding: 18px 0 0 40px;
    color: var(--white);
  }
  .identity__name {
    font-family: "Oswald", sans-serif;
    font-weight: 500;
    font-size: 30px;
    line-height: 1;
    letter-spacing: 1px;
    text-transform: uppercase;
  }
  .identity__role {
    font-family: "Exo 2", sans-serif;
    font-size: 11px;
    letter-spacing: 2px;
    text-transform: uppercase;
    margin-top: 4px;
  }

  .contacts {
    position: absolute;
    left: 416px;
    top: 152px;
    width: 188px;
    height: 152px;
    background: var(--navy);
    list-style: none;
    padding: 14px 10px 0 8px;
  }
  .contacts__item {
    display: flex;
    justify-content: flex-end;
    align-items: center;
    gap: 6px;
    height: 30px;
    font-family: "Exo 2", sans-serif;
    font-size: 9.5px;
    color: var(--white);
    letter-spacing: 0.3px;
    white-space: nowrap;
  }
  .contacts__icon {
    flex: none;
    width: 14px;
    height: 14px;
    background: var(--white);
    display: flex;
    align-items: center;
    justify-content: center;
  }
  .contacts__icon svg { width: 10px; height: 10px; fill: var(--navy); stroke: var(--navy); }
</style>
</head>
<body>

<section class="card card--front" aria-label="Business card front">
  <div class="band front__top"></div>
  <p class="company-name front__name">Kelmscott</p>
  <div class="band front__rule"></div>
  <div class="band front__bottom"></div>
</section>

<section class="card card--back" aria-label="Business card back">
  <div class="band back__top"></div>

  <p class="offices">Kelmscott House, 17 Birchcombe, Pinner. HA5 3QX<br>Veltris Centre, Marlowe Lane, Hebburn, NE31 4GT</p>

  <div class="band back__divider"></div>
  <div class="back__panel"></div>

  <p class="company-name back__name">Kelmscott</p>

  <div class="identity">
    <p class="identity__name">Simon Trewella</p>
    <p class="identity__role">General Manager</p>
  </div>

  <ul class="contacts">
    <li class="contacts__item">M 0044 7700 318 642
      <span class="contacts__icon"><svg viewBox="0 0 10 10"><path stroke="none" d="M2 0.5 L3.6 2.6 L2.8 3.6 Q4 5.8 6.4 7.2 L7.4 6.4 L9.5 8 L8.4 9.5 Q4.5 9.3 1.6 5.6 Q0.3 3.6 0.6 1.5 Z"/></svg></span>
    </li>
    <li class="contacts__item">London 00 44 20 718 46203
      <span class="contacts__icon"><svg viewBox="0 0 10 10"><path stroke="none" d="M2 0.5 L3.6 2.6 L2.8 3.6 Q4 5.8 6.4 7.2 L7.4 6.4 L9.5 8 L8.4 9.5 Q4.5 9.3 1.6 5.6 Q0.3 3.6 0.6 1.5 Z"/></svg></span>
    </li>
    <li class="contacts__item">North East 00 44 191 4826053
      <span class="contacts__icon"><svg viewBox="0 0 10 10"><path stroke="none" d="M2 0.5 L3.6 2.6 L2.8 3.6 Q4 5.8 6.4 7.2 L7.4 6.4 L9.5 8 L8.4 9.5 Q4.5 9.3 1.6 5.6 Q0.3 3.6 0.6 1.5 Z"/></svg></span>
    </li>
    <li class="contacts__item">www.kelmscotttalent-example.com
      <span class="contacts__icon"><svg viewBox="0 0 10 10"><circle cx="5" cy="5" r="4.2" fill="none" stroke-width="0.9"/><ellipse cx="5" cy="5" rx="1.8" ry="4.2" fill="none" stroke-width="0.8"/><path d="M0.8 5 H9.2" stroke-width="0.8"/></svg></span>
    </li>
  </ul>
</section>

</body>
</html>
```